Manufacturer's Representative Group needs a clean new Website

We represent and sell a number of suppliers that design and build products used in Biopharmaceutical manufacturing. Our sales region is in the central US. Our customer base is scientific / engineering based - so clean, we organized design with a focus on the products - easy and clear navigation is necessary. We do not sell direct or warehouse product - so e-commerce is not needed. Our customers will use the website for reference on what we do and offer - we will use the site as a platform to present products from each vendor and the home page will be used to capture an overview and draw users deeper into the site. You can view our current site - which needs A LOT of help to get ideas on products represented and types of products

Target Market(s)

Engineers and Pharmaceutical / Bio pharm end users

Industry/Entity Type

E-Commerce

Number of Pages Required

2 page

Font styles to use
Sans Serif

Requirements
Must have
• I need a home page that provides a snapshot of my company and the product lines we represent - then a second page that I can copy as a template for each line I rep as well as for an "About us / contact" page.
• I would like to be able to manage content on the pages so something easy to adjust pictures or add content is a must
• Must use our logo

```html
<!DOCTYPE html>
<html lang="en">
<head>
<meta charset="utf-8">
<title>Prairie Bio</title>
<link href="https://fonts.googleapis.com/css2?family=Lato:wght@300;400;700;900&display=swap" rel="stylesheet">
<style>
:root{
  --navy:#15305b;
  --navy-deep:#1b2659;
  --orange:#f26522;
  --blue:#2a5da8;
  --page:#f2f2f2;
  --ink:#222;
  --muted:#666;
  --light:#cfd8e6;
}
*{box-sizing:border-box;margin:0;padding:0}
html,body{width:1200px;height:2988px;overflow:hidden}
body{position:relative;background:var(--page);font-family:'Lato',sans-serif;color:var(--ink)}
.abs{position:absolute}
svg{display:block}

/* header */
.brand{left:78px;top:38px;display:flex;align-items:center;gap:18px}
.brand-mark{width:70px;height:70px;border-radius:50%;background:var(--orange)}
.brand-name{font-size:64px;font-weight:700;color:var(--navy-deep);letter-spacing:-1px}
.social-top{right:80px;top:36px;display:flex;gap:12px}
.social-dot{width:40px;height:40px;border-radius:50%;background:var(--navy-deep)}
.phone-top{right:80px;top:92px;display:flex;align-items:center;gap:12px;font-size:30px;font-weight:700;color:var(--orange)}

.nav{left:40px;top:146px;width:1100px;height:54px;background:var(--orange);display:flex;align-items:center}
.nav a{display:block;color:#fff;text-decoration:none;font-size:13px;text-transform:uppercase;line-height:54px;white-space:nowrap;text-align:center}
.nav a.active{background:var(--navy-deep);width:123px}
.nav .gap{margin-left:62px}
.nav .gap2{margin-left:74px}
.search{margin-left:auto;display:flex;height:38px;margin-right:2px}
.search span{width:282px;background:#fff;display:block}
.search b{width:36px;background:var(--navy-deep);display:flex;align-items:center;justify-content:center}

/* hero */
.hero{left:40px;top:200px;width:1115px;height:418px;background:linear-gradient(135deg,#cfe4f2 0%,#6fa8d4 40%,#2f6fa8 75%,#184a80 100%)}
.hero-caption{left:155px;top:311px;width:500px;height:224px;background:rgba(21,48,91,.55);color:#fff;padding:30px 32px}
.hero-caption h2{font-size:26px;font-weight:700;margin-bottom:18px;letter-spacing:.5px}
.hero-caption p{font-size:14px;line-height:1.5;color:#e5edf6}
.hero-dots{right:100px;top:590px;display:flex;gap:8px}
.hero-dots i{width:14px;height:14px;background:var(--navy-deep);display:block}
.hero-dots i:first-child{background:var(--orange)}

/* features */
.feature{top:712px;width:290px;text-align:center}
.feature h3{font-size:24px;font-weight:700;color:#111;text-transform:uppercase;margin-bottom:30px}
.feature svg{margin:0 auto 24px}
.feature p{font-size:13.5px;line-height:1.5;color:#555}
.tag{width:38px;height:26px;background:var(--navy-deep)}

/* products */
.products-band{left:0;top:1040px}
.products-title{left:0;top:1104px;width:1200px;display:flex;align-items:center;justify-content:center;gap:28px;color:#fff}
.products-title i{width:320px;height:1px;background:#9fb0c9;display:block}
.products-title h2{font-size:30px;font-weight:700;text-transform:uppercase;line-height:36px}
.product{top:1175px;width:230px;text-align:center;color:#fff}
.product-photo{width:190px;height:190px;border-radius:50%;border:6px solid #fff;margin:0 auto 20px;background:radial-gradient(circle at 50% 45%,#ffffff 0%,#e8edf4 45%,#b9c8db 100%)}
.product h4{font-size:15px;font-weight:700;text-transform:uppercase;padding-bottom:10px;border-bottom:1px solid #6d86ab;margin-bottom:10px}
.product p{font-size:13px;line-height:1.5;color:#d4ddea}
.pager{display:flex;gap:10px}
.pager b{width:64px;height:34px;background:#8ea0ba;color:#fff;display:flex;align-items:center;justify-content:center;font-size:18px}
.pager.dark b{width:44px;height:28px;background:var(--navy-deep);font-size:14px}

/* welcome */
.welcome{left:87px;top:1672px;width:540px}
.welcome small{display:block;font-size:26px;font-weight:300;color:#444;text-transform:uppercase}
.welcome h2{font-size:50px;font-weight:300;color:var(--orange);text-transform:uppercase;line-height:1.05;margin-bottom:16px}
.welcome p{font-size:14px;line-height:1.55;color:#333}
.lab-photo{left:660px;top:1681px;width:478px;height:316px;border:2px solid var(--navy-deep);background:linear-gradient(120deg,#2c3f63 0%,#7e93b4 45%,#c9d3e2 70%,#5f6f8d 100%)}

/* newsletter */
.news-title{left:0;top:2154px;width:1200px;display:flex;align-items:center;justify-content:center;gap:22px;color:#fff}
.news-title i{width:330px;height:1px;background:#8da0bd;display:block}
.news-title h2{font-size:20px;font-weight:400;text-transform:uppercase;letter-spacing:.5px}
.subscribe{left:281px;top:2224px;display:flex;height:40px}
.subscribe span{width:436px;background:#fff;font-size:14px;color:#999;padding:0 20px;line-height:40px}
.subscribe b{width:170px;background:var(--orange);color:#fff;font-size:15px;text-transform:uppercase;display:flex;align-items:center;justify-content:center}

/* news & testimonials */
.col-title{top:2345px;font-size:32px;font-weight:300;color:var(--orange);text-transform:uppercase;padding-bottom:10px;border-bottom:1px solid #bbb}
.news-item{left:75px;width:540px;display:flex;gap:22px}
.news-thumb{width:150px;height:112px;flex:none}
.news-item h4{font-size:14px;font-weight:700;text-transform:uppercase;margin-bottom:6px}
.news-item em{display:block;font-style:italic;font-size:13px;color:var(--orange);margin-bottom:6px}
.news-item p{font-size:12.5px;line-height:1.5;color:#777}
.divider{left:655px;top:2350px;height:330px;border-left:2px dashed #999}
.quote{left:690px;top:2420px;width:420px;display:flex;gap:18px}
.quote-mark{width:32px;height:32px;background:var(--orange);color:#fff;font-size:30px;font-weight:900;line-height:40px;text-align:center;flex:none}
.quote p{font-size:13px;line-height:1.5;color:#888;padding-bottom:16px;border-bottom:1px solid #aaa}
.author{left:725px;top:2570px;display:flex;align-items:center;gap:18px}
.avatar{width:90px;height:90px;border-radius:50%;border:4px solid #fff;background:linear-gradient(160deg,#d9a98a,#8a6a58)}
.author h5{font-size:15px;font-weight:700;text-transform:uppercase}
.author span{font-size:13px;font-style:italic;color:var(--orange)}
.chev{font-size:16px;color:var(--orange);font-weight:700}

/* footer */
.footer-social{left:0;top:2815px;width:1200px;display:flex;justify-content:center;gap:30px}
.footer-social i{width:46px;height:46px;border-radius:50%;background:#fff;display:block}
.footer-contact{left:0;top:2888px;width:1200px;display:flex;justify-content:center;align-items:center;gap:14px;color:#fff}
.footer-contact .addr{font-size:15px;margin-right:70px}
.footer-contact .tel{font-size:30px;font-weight:400}
.copyright{left:0;top:2957px;width:1200px;text-align:center;font-size:13px;color:#fff}
</style>
</head>
<body>

<header>
  <div class="abs brand"><span class="brand-mark"></span><span class="brand-name">Prairie Bio</span></div>
  <div class="abs social-top"><i class="social-dot"></i><i class="social-dot"></i><i class="social-dot"></i><i class="social-dot"></i></div>
  <div class="abs phone-top">
    <svg width="28" height="28" viewBox="0 0 24 24"><path fill="#f26522" d="M6.6 10.8a15.1 15.1 0 0 0 6.6 6.6l2.2-2.2c.3-.3.7-.4 1-.2 1.1.4 2.3.6 3.6.6.6 0 1 .4 1 1V20c0 .6-.4 1-1 1A17 17 0 0 1 3 4c0-.6.4-1 1-1h3.5c.6 0 1 .4 1 1 0 1.3.2 2.5.6 3.6.1.3 0 .7-.2 1z"/></svg>
    1-800-555-0147
  </div>
  <nav class="abs nav">
    <a class="active">Home</a><a class="gap" style="margin-left:80px">About us</a><a class="gap">Products</a><a class="gap">Research</a><a class="gap">Blog</a><a class="gap">Contact us</a>
    <div class="search"><span></span><b><svg width="16" height="16" viewBox="0 0 16 16"><path d="M4 14 14 14 14 4Z" fill="#fff"/></svg></b></div>
  </nav>
</header>

<section class="hero-wrap">
  <svg class="abs" style="left:0;top:200px" width="1200" height="440">
    <polygon points="0,60 40,80 40,418 0,380" fill="#f26522"/>
    <polygon points="0,180 40,200 40,418 0,330" fill="#2a5da8"/>
    <polygon points="1155,0 1200,0 1200,300 1155,330" fill="#2a5da8"/>
    <polygon points="1155,150 1200,130 1200,260 1155,300" fill="#f26522"/>
  </svg>
  <div class="abs hero" role="img" aria-label="Laboratory glassware in blue light"></div>
  <svg class="abs" style="left:40px;top:200px" width="1115" height="418">
    <polygon points="0,300 420,418 0,418" fill="#1b2659" opacity=".6"/>
    <polygon points="700,418 1115,300 1115,418" fill="#e9edf2"/>
    <polyline points="60,140 30,170 60,200" fill="none" stroke="#fff" stroke-width="2"/>
    <polyline points="1060,140 1090,170 1060,200" fill="none" stroke="#fff" stroke-width="2"/>
  </svg>
  <div class="abs hero-caption">
    <h2>LABORATORY</h2>
    <p>Sed ut perspiciatis unde omnis iste natus error sit voluptatem accusantium doloremque laudantium, totam rem aperiam, eaque ipsa quae ab illo inventore veritatis et quasi architecto beatae vitae dicta sunt explicabo. Nemo enim ipsam voluptatem quia voluptas.</p>
  </div>
  <div class="abs tag" style="left:617px;top:509px"></div>
  <div class="abs hero-dots"><i></i><i></i><i></i><i></i></div>
</section>

<section class="features">
  <div class="abs feature" style="left:100px">
    <h3>Laboratory</h3>
    <svg width="60" height="80" viewBox="0 0 60 80"><path d="M22 4h16M25 4v26L6 70a5 5 0 0 0 4 7h40a5 5 0 0 0 4-7L35 30V4" fill="none" stroke="#1b2659" stroke-width="5"/><path d="M14 56h32l6 14H8z" fill="#1b2659"/></svg>
    <p>Sed ut perspiciatis unde omnis iste natus error sit voluptatem accusantium doloremque laudantium, totam rem aperiam, eaque ipsa quae ab illo inventore veritatis et quasi</p>
  </div>
  <div class="abs tag" style="left:370px;top:985px"></div>
  <div class="abs feature" style="left:455px">
    <h3>Researches</h3>
    <svg width="70" height="80" viewBox="0 0 70 80"><rect x="26" y="4" width="14" height="36" rx="3" transform="rotate(25 33 22)" fill="#1b2659"/><path d="M20 48h20M30 48v16M42 30a22 22 0 0 1 0 34M8 74h54" fill="none" stroke="#1b2659" stroke-width="6"/></svg>
    <p>Perspiciatis unde omnis iste natuerror sit voluatem accusantium doloremque laudanm, totam rem aperiam, eaque ipsa quae ab illo inventatis et quasi arch beatae vitae</p>
  </div>
  <div class="abs tag" style="left:720px;top:985px"></div>
  <div class="abs feature" style="left:800px">
    <h3>Technologies</h3>
    <svg width="80" height="80" viewBox="0 0 80 80"><path d="M14 40 38 30 44 62M38 30 64 12" stroke="#1b2659" stroke-width="4"/><circle cx="14" cy="40" r="8" fill="#1b2659"/><circle cx="38" cy="30" r="10" fill="#1b2659"/><circle cx="44" cy="64" r="8" fill="#1b2659"/><circle cx="66" cy="12" r="8" fill="#1b2659"/></svg>
    <p>Sed ut perspiciatis unde omnis iste natus error sit voluptatem accusantium doloremque laudantium, totam rem aperiam, eaque ipsa quae ab illo inventore veritatis et quasi</p>
  </div>
  <div class="abs tag" style="left:1070px;top:985px"></div>
</section>

<section class="products">
  <svg class="abs products-band" width="1200" height="570">
    <polygon points="0,0 1200,0 1200,470 0,500" fill="#15305b"/>
    <polygon points="0,470 600,505 0,540" fill="#f26522"/>
    <polygon points="0,500 1200,470 1200,525 0,560" fill="#2a5da8"/>
    <polygon points="650,500 1200,450 1200,480" fill="#f26522"/>
  </svg>
  <svg class="abs" style="left:582px;top:1076px" width="36" height="20" viewBox="0 0 36 20"><rect x="1" y="1" width="34" height="18" rx="9" fill="none" stroke="#fff" stroke-width="2"/><path d="M18 1h8a9 9 0 0 1 0 18h-8z" fill="#fff"/></svg>
  <div class="abs products-title"><i></i><h2>Products</h2><i></i></div>
  <div class="abs product" style="left:47px"><div class="product-photo" role="img" aria-label="Product vial and carton"></div><h4>Doloremque laudan</h4><p>Sed ut perspiciatis unde omnis iste natus error sit voluptatem accusantium doloremque laudantium, totam rem aperiam, eaque ipsa quae ab illo</p></div>
  <div class="abs product" style="left:345px"><div class="product-photo" role="img" aria-label="Product vial bottle"></div><h4>Doloremque laudan</h4><p>Sed ut perspiciatis unde omnis iste natus error sit voluptatem accusantium doloremque laudantium, totam rem aperiam, eaque ipsa quae ab illo</p></div>
  <div class="abs product" style="left:632px"><div class="product-photo" role="img" aria-label="Product vial and carton"></div><h4>Doloremque laudan</h4><p>Sed ut perspiciatis unde omnis iste natus error sit voluptatem accusantium doloremque laudantium, totam rem aperiam, eaque ipsa quae ab illo</p></div>
  <div class="abs product" style="left:911px"><div class="product-photo" role="img" aria-label="Product vial bottle"></div><h4>Doloremque laudan</h4><p>Sed ut perspiciatis unde omnis iste natus error sit voluptatem accusantium doloremque laudantium, totam rem aperiam, eaque ipsa quae ab illo</p></div>
  <div class="abs pager" style="left:530px;top:1520px"><b>&lt;</b><b>&gt;</b></div>
</section>

<section>
  <div class="abs welcome">
    <small>Welcome to</small>
    <h2>Prairie Bio</h2>
    <p>The purpose of the Central Bioprocess Statistics Forum is to foster discussion on statistical methodology in the pharmaceutical industry. The next edition is May 19-21, 2014. The first annual conference was held in 1978. The founders decided to proceed with a conference emphasis on the applications and theory relevant to the pharmaceutical industry. Since the pharmaceutical industry spanned a wide range of research and development activity – basic biological and chemical research, clinical research, process development, assay development, dosage form development, stability, quality control, quality assurance, and manufacturing – it was decided that at least three "parallel tracks" were necessary in order to better serve the pharmaceutical statisticians. The founders also pledged to provide opportunities for</p>
  </div>
  <div class="abs tag" style="left:585px;top:1990px;width:42px;height:30px"></div>
  <div class="abs lab-photo" role="img" aria-label="Scientist working with laboratory equipment"></div>
</section>

<section>
  <svg class="abs" style="left:0;top:2085px" width="1200" height="240">
    <polygon points="0,0 1200,20 1200,200 0,235" fill="#15305b"/>
  </svg>
  <svg class="abs" style="left:582px;top:2120px" width="36" height="26" viewBox="0 0 36 26"><rect width="36" height="26" fill="#fff"/><path d="M0 0 18 14 36 0" fill="none" stroke="#15305b" stroke-width="2"/></svg>
  <div class="abs news-title"><i></i><h2>Subscribe to our news letter</h2><i></i></div>
  <div class="abs subscribe"><span>Enter your email address</span><b>Submit</b></div>
</section>

<section>
  <h2 class="abs col-title" style="left:95px;width:520px">Latest news</h2>
  <div class="abs news-item" style="top:2428px">
    <div class="news-thumb" role="img" aria-label="Coloured liquids in laboratory flasks" style="background:linear-gradient(90deg,#7fa7c9,#d9c36a,#c96a5a,#6a9ac9)"></div>
    <div><h4>Oque penatibus et magnis dis parturient</h4><em>27 DEC 2014</em><p>Praesent vestibulum aenean nonummy hendrerit mauris. Cum sociis natoque penatibus et magnis dis parturient montes ascetur ridiculus mus. Nulla dui. Fusce feugiat malesuada odio. Morbi nunc odio gravida at cursus nec luctus a lorem</p></div>
  </div>
  <div class="abs news-item" style="top:2565px">
    <div class="news-thumb" role="img" aria-label="White tablets and capsules" style="background:linear-gradient(135deg,#f4f4f4,#d8dbe0,#b6bcc6)"></div>
    <div><h4>Oque penatibus et magnis dis parturient</h4><em>27 DEC 2014</em><p>Praesent vestibulum aenean nonummy hendrerit mauris. Cum sociis natoque penatibus et magnis dis parturient montes ascetur ridiculus mus. Nulla dui. Fusce feugiat malesuada odio. Morbi nunc odio gravida at cursus nec luctus a lorem</p></div>
  </div>
  <div class="abs pager dark" style="left:535px;top:2687px"><b>&lt;</b><b>&gt;</b></div>

  <div class="abs divider"></div>
  <h2 class="abs col-title" style="left:692px;width:420px">Testimonials</h2>
  <div class="abs quote"><span class="quote-mark">“</span><p>Praesent vestibulum aenean nonummy hendrerit mauris. Cum sociis natoque penatibus et magnis dis parturient montes ascetur ridiculus mus. Nulla dui. Fusce feugiat malesuada odio. Morbi nunc odio</p></div>
  <span class="abs chev" style="left:698px;top:2604px">‹</span>
  <div class="abs author"><div class="avatar" role="img" aria-label="Portrait of the reviewer"></div><div><h5>Dr. Martin Hale</h5><span>Biopharmacist</span></div></div>
  <span class="abs chev" style="left:1010px;top:2604px">›</span>
</section>

<footer>
  <svg class="abs" style="left:0;top:2720px" width="1200" height="268">
    <polygon points="0,10 700,50 0,60" fill="#f26522"/>
    <polygon points="0,40 1200,30 1200,70 0,80" fill="#2a5da8"/>
    <polygon points="0,60 1200,55 1200,268 0,268" fill="#15305b"/>
  </svg>
  <div class="abs footer-social"><i></i><i></i><i></i><i></i></div>
  <div class="abs footer-contact">
    <svg width="28" height="24" viewBox="0 0 28 24"><path d="M14 1 1 12h4v11h7v-7h4v7h7V12h4z" fill="#fff"/></svg>
    <span class="addr">Harbor Hall Clearfield, Ohio, United States</span>
    <svg width="28" height="28" viewBox="0 0 24 24"><path fill="#fff" d="M6.6 10.8a15.1 15.1 0 0 0 6.6 6.6l2.2-2.2c.3-.3.7-.4 1-.2 1.1.4 2.3.6 3.6.6.6 0 1 .4 1 1V20c0 .6-.4 1-1 1A17 17 0 0 1 3 4c0-.6.4-1 1-1h3.5c.6 0 1 .4 1 1 0 1.3.2 2.5.6 3.6.1.3 0 .7-.2 1z"/></svg>
    <span class="tel">1-800-555-0147</span>
  </div>
  <p class="abs copyright">© 2014 prairie bio | privacy policy</p>
</footer>

</body>
</html>
```